Web App UI Design prototype

I have a sketch of a series of pages for a new web app, and would like to develop a clean, user friendly, intuitive design around the content.

Target Market(s)

small to medium sized business owners

Number of Pages Required

5+ page

Font styles to use
Sans Serif

Colors
33a6d7
85cae6
33b8a4
86cfc6
886aae
faa54b
000000
757575
cbcbcb

Requirements
Must have
• Color pallet that fits with my logo
• Clean modern, timeless design
• Intuitive use of UI
• Icons always help

```html
<!DOCTYPE html>
<html lang="en">
<head>
<meta charset="utf-8">
<title>Wrennfold – Process</title>
<link href="https://fonts.googleapis.com/css2?family=Open+Sans:wght@400;600&display=swap" rel="stylesheet">
<style>
:root{
  --blue:#33a6d7;
  --purple:#886aae;
  --orange:#faa54b;
  --grey:#757575;
  --line:#cbcbcb;
  --side:#f5f5f5;
  --band:#ebebeb;
  --ink:#222;
  --muted:#555;
}
*{box-sizing:border-box;margin:0;padding:0}
html,body{width:1200px;height:957px;overflow:hidden}
body{font-family:"Open Sans",sans-serif;background:var(--band);position:relative;color:var(--ink)}
.brand{position:absolute;left:0;top:0;width:240px;height:131px;background:var(--side);border-bottom:1px solid #ddd;display:flex;align-items:center;gap:10px;padding-left:34px}
.brand-dot{width:18px;height:18px;border-radius:50%;background:var(--blue);flex:none}
.brand-name{font-size:30px;font-weight:400;color:var(--blue)}
.topbar{position:absolute;left:240px;top:0;width:960px;height:131px;background:var(--grey);color:#fff}
.org{position:absolute;left:24px;top:50px;display:flex;align-items:center;gap:12px;font-size:21px}
.search{position:absolute;left:195px;top:44px;width:298px;height:41px;border-radius:21px;background:#ebebeb;display:flex;align-items:center;justify-content:space-between;padding:0 16px;color:#444;font-size:16px}
.nav-link{position:absolute;top:50px;display:flex;align-items:center;gap:8px;font-size:21px}
.home{left:552px}.dash{left:712px}
.gear{position:absolute;left:909px;top:51px}
.sidebar{position:absolute;left:0;top:131px;width:240px;height:763px;background:var(--side)}
.run{position:absolute;left:35px;top:33px;width:170px;height:41px;border-radius:21px;background:var(--orange);color:#fff;font-size:20px;display:flex;align-items:center;justify-content:center;gap:8px}
.group-head{position:absolute;left:0;width:240px;height:48px;background:var(--band);display:flex;align-items:center;justify-content:space-between;padding:0 16px 0 23px;color:var(--blue);font-size:20px}
.group-list{position:absolute;left:23px;list-style:none}
.group-list li{height:40px;display:flex;align-items:center;gap:10px;font-size:15px;color:#333}
.tabs{position:absolute;left:264px;top:155px;width:913px;height:48px;background:#fff;border-bottom:2px solid var(--purple);display:flex}
.tab{height:46px;display:flex;align-items:center;justify-content:center;font-size:19px;color:#666;border-right:1px solid #e4e4e4}
.tab.active{background:var(--purple);color:#fff}
.title{position:absolute;left:264px;top:246px;font-size:21px;font-weight:400}
.filters{position:absolute;left:736px;top:244px;display:flex;gap:8px}
.filter{width:104px;height:34px;background:#fff;border:1px solid #ddd;display:flex;align-items:center;justify-content:space-between;padding:0 10px 0 13px;font-size:11px;color:#666}
.table{position:absolute;left:264px;top:286px;width:912px;border-collapse:collapse;background:#fff}
.table th{height:46px;background:#f5f5f5;text-align:left;font-weight:600;font-size:15px;color:var(--muted)}
.table td{height:46px;font-size:13px;color:var(--grey);border-top:1px solid #e4e4e4}
.table th+th,.table td+td{border-left:1px solid #e4e4e4}
.c1{width:147px;padding-left:24px}.c2{width:185px;padding-left:37px}.c3{width:345px;padding-left:52px}.c4{padding-left:43px}
.footer{position:absolute;left:0;top:894px;width:1200px;height:63px;background:var(--grey);color:#fff;font-size:11px;text-align:center;padding-top:29px}
.footer .ver{position:absolute;right:10px;top:38px}
</style>
</head>
<body>
<header class="brand"><span class="brand-dot"></span><span class="brand-name">Wrennfold</span></header>
<div class="topbar">
  <div class="org">
    <svg width="20" height="18" viewBox="0 0 20 18" fill="#fff"><rect y="0" width="20" height="3" rx="1"/><rect y="7.5" width="20" height="3" rx="1"/><rect y="15" width="20" height="3" rx="1"/></svg>
    KORVASTEL
  </div>
  <div class="search">Search
    <svg width="16" height="16" viewBox="0 0 16 16" fill="none" stroke="#555" stroke-width="2.2"><circle cx="6.5" cy="6.5" r="5"/><path d="M10.5 10.5l4 4"/></svg>
  </div>
  <div class="nav-link home">
    <svg width="22" height="18" viewBox="0 0 22 18" fill="#fff"><path d="M11 0L0 9h3v9h6v-6h4v6h6V9h3z"/></svg>Home
  </div>
  <div class="nav-link dash">
    <svg width="24" height="18" viewBox="0 0 24 18"><path d="M12 0A12 12 0 0 0 0 12v6h24v-6A12 12 0 0 0 12 0z" fill="#fff"/><circle cx="5" cy="11" r="1.6" fill="#757575"/><circle cx="8" cy="5.5" r="1.6" fill="#757575"/><circle cx="16" cy="5.5" r="1.6" fill="#757575"/><circle cx="19" cy="11" r="1.6" fill="#757575"/><path d="M12 14l3-8" stroke="#757575" stroke-width="2"/></svg>Dashboard
  </div>
  <svg class="gear" width="28" height="28" viewBox="0 0 28 28"><g fill="#fff" transform="translate(14 14)"><rect x="-3" y="-14" width="6" height="28" rx="1"/><rect x="-3" y="-14" width="6" height="28" rx="1" transform="rotate(45)"/><rect x="-3" y="-14" width="6" height="28" rx="1" transform="rotate(90)"/><rect x="-3" y="-14" width="6" height="28" rx="1" transform="rotate(135)"/><circle r="10"/></g><circle cx="14" cy="14" r="4" fill="#757575"/></svg>
</div>

<nav class="sidebar">
  <div class="run"><svg width="18" height="18" viewBox="0 0 18 18"><circle cx="9" cy="9" r="9" fill="#fff"/><path d="M7 5l6 4-6 4z" fill="#faa54b"/></svg>RUN</div>
  <div class="group-head" style="top:106px">DEPARTMENTS<svg width="12" height="7"><path d="M0 0h12L6 7z" fill="#33a6d7"/></svg></div>
  <ul class="group-list" style="top:160px">
    <li><svg width="5" height="9"><path d="M1 1l3 3.5L1 8" stroke="#333" fill="none"/></svg>Sales &amp; Modeling</li>
    <li><svg width="5" height="9"><path d="M1 1l3 3.5L1 8" stroke="#333" fill="none"/></svg>Operations</li>
    <li><svg width="5" height="9"><path d="M1 1l3 3.5L1 8" stroke="#333" fill="none"/></svg>Finance</li>
    <li><svg width="5" height="9"><path d="M1 1l3 3.5L1 8" stroke="#333" fill="none"/></svg>Admin</li>
  </ul>
  <div class="group-head" style="top:338px">PROCESSES<svg width="12" height="7"><path d="M0 0h12L6 7z" fill="#33a6d7"/></svg></div>
  <ul class="group-list" style="top:392px">
    <li><svg width="5" height="9"><path d="M1 1l3 3.5L1 8" stroke="#333" fill="none"/></svg>All</li>
    <li><svg width="5" height="9"><path d="M1 1l3 3.5L1 8" stroke="#333" fill="none"/></svg>Saved</li>
    <li><svg width="5" height="9"><path d="M1 1l3 3.5L1 8" stroke="#333" fill="none"/></svg>Recent</li>
  </ul>
</nav>

<main>
  <div class="tabs">
    <div class="tab" style="width:101px">Map</div>
    <div class="tab active" style="width:126px">Process</div>
    <div class="tab" style="width:114px">Team</div>
    <div class="tab" style="width:120px">Tables</div>
  </div>
  <h1 class="title">Pingvale Post</h1>
  <div class="filters">
    <div class="filter">Dept<svg width="9" height="6"><path d="M1 1l3.5 3.5L8 1" stroke="#666" fill="none"/></svg></div>
    <div class="filter">Statuses<svg width="9" height="6"><path d="M1 1l3.5 3.5L8 1" stroke="#666" fill="none"/></svg></div>
    <div class="filter">Assignees<svg width="9" height="6"><path d="M1 1l3.5 3.5L8 1" stroke="#666" fill="none"/></svg></div>
    <div class="filter">Dates<svg width="9" height="6"><path d="M1 1l3.5 3.5L8 1" stroke="#666" fill="none"/></svg></div>
  </div>
  <table class="table">
    <thead><tr><th class="c1">Name</th><th class="c2">Date Created</th><th class="c3">Link to Content</th><th class="c4">Created By</th></tr></thead>
    <tbody>
      <tr><td class="c1">Promotion</td><td class="c2">1 August, 2017</td><td class="c3">http://pingvale.com</td><td class="c4">Marcus</td></tr>
      <tr><td class="c1">Throwback Thurs</td><td class="c2">25 July, 2017</td><td class="c3">http://pingvale.com</td><td class="c4">Marcus</td></tr>
    </tbody>
  </table>
</main>

<footer class="footer">Copyright &copy; 2017 &nbsp;Wrennfold. &nbsp;All rights reserved.<span class="ver">M2</span></footer>
</body>
</html>
```